Educational Data Analysis Trade Show Booth

Trade show booth is 90"w x 101"h. We need a clean, modern design that will shout: education and functionable data. Our company takes data such as test scores, attendance, expenditures over a period of time and does an analysis, and presents it in a very easy to follow form.
Our website is https://brightmarkpartners-llc.example
The booth we have is at https://exhibitframeco.example/collections/8ft-portable-expo-panels-expo-stand-backdrops/products/8ft-snapframe-pro-arched?variant=58219047736120
The design will be for the backdrop, the top banner, the side shelf rack and the podium.
Our tag line is: Grounded Insight Mapping
Updates

Our product is called "Holistic Gap Profile Report" that needs to be on there somewhere. I would love a QR code that takes them to our sample on our website. www.brightmarkpartners-llc.example
Somewhere on the board needs to have our Name: Brightmark Partners "logo"
Our product: Holistic Gap Profile Report
Our tag line: Practical Insight Mapping

This project has been extended in hopes to find one to work with. This does have to be available in either Photoshop or Illustrator for the company we are using.

Target Market(s)

Education

Industry/Entity Type

Education

Requirements
Must have
• Holistic Gap Profile Report (this is our actual product)
Nice to have
• A QR that takes the client to the sample on our website listed in the project description

```html
<!DOCTYPE html>
<html lang="en">
<head>
<meta charset="UTF-8">
<title>Holistic Gap Profile Report – Brightmark Partners</title>
<link rel="stylesheet" href="https://fonts.googleapis.com/css2?family=Montserrat:wght@400;500;600;700&display=swap">
<style>
  :root {
    --bg: #f5f6f8;
    --ink: #1e1e1e;
    --green: #a8c945;
    --green-deep: #8dbb43;
    --white: #ffffff;
    --navy: #0f2a44;
    --teal: #19a2bd;
    --orange: #f0952b;
  }
  * { margin: 0; padding: 0; box-sizing: border-box; }
  html, body { width: 1200px; height: 1068px; overflow: hidden; background: var(--bg); }
  .backdrop {
    position: relative;
    width: 1200px;
    height: 1068px;
    background: var(--bg);
    font-family: "Montserrat", sans-serif;
    color: var(--ink);
    overflow: hidden;
  }
  .sweeps { position: absolute; inset: 0; width: 1200px; height: 1068px; }
  .product-title {
    position: absolute;
    left: 36px;
    top: 26px;
    font-weight: 700;
    font-size: 72px;
    line-height: 86px;
    letter-spacing: 2px;
  }
  .tagline {
    position: absolute;
    left: 36px;
    top: 214px;
    font-weight: 600;
    font-size: 36px;
    letter-spacing: 1.5px;
  }
  .features {
    position: absolute;
    left: 36px;
    top: 311px;
    display: flex;
    align-items: center;
  }
  .feature { display: flex; align-items: center; gap: 18px; }
  .feature-badge {
    width: 50px; height: 50px;
    border-radius: 50%;
    border: 3px solid var(--green);
    background: var(--white);
    display: flex; align-items: center; justify-content: center;
    flex: none;
  }
  .feature-label {
    font-weight: 500;
    font-size: 21px;
    line-height: 28px;
    letter-spacing: 1px;
  }
  .divider {
    width: 2px; height: 32px;
    background: var(--ink);
    margin: 0 20px 0 20px;
  }
  .website {
    position: absolute;
    left: 36px;
    top: 456px;
    display: flex;
    align-items: center;
    gap: 18px;
    font-size: 25px;
    letter-spacing: 3px;
  }
  .globe {
    width: 32px; height: 32px; border-radius: 50%;
    background: var(--green);
    display: flex; align-items: center; justify-content: center;
  }
  .website strong { font-weight: 700; }
  .team-scene {
    position: absolute;
    left: 36px;
    top: 532px;
    width: 712px;
    height: 500px;
    border-radius: 40px 40px 50% 50% / 40px 40px 60px 60px;
    background: linear-gradient(180deg, #dfe6ee 0%, #a9b9c7 55%, #8dbb43 100%);
  }
</style>
</head>
<body>
<main class="backdrop">
  <svg class="sweeps" viewBox="0 0 2044 1819" preserveAspectRatio="none" aria-hidden="true">
    <path d="M1105 0 C1260 190 1480 250 1700 230 C1820 218 1930 170 2044 90 L2044 0 Z" fill="var(--green)"/>
    <path d="M1190 0 C1340 160 1530 215 1720 200 C1810 192 1880 172 1920 160" fill="none" stroke="var(--bg)" stroke-width="10"/>
    <path d="M0 1135 Q700 1420 1350 1140 Q1800 900 2044 370 L2044 1819 L0 1819 Z" fill="var(--green)"/>
    <path d="M0 1285 Q700 1470 1350 1180 Q1820 950 2044 405 L2044 670 Q1800 1030 1400 1240 Q750 1570 0 1310 Z" fill="var(--bg)"/>
    <path d="M1300 1819 Q1620 1570 2044 1545" fill="none" stroke="var(--bg)" stroke-width="16"/>
    <path d="M1330 1819 Q1650 1590 2044 1575 L2044 1819 Z" fill="var(--bg)"/>
  </svg>

  <h1 class="product-title">Holistic Gap<br>Profile Report</h1>
  <p class="tagline">Grounded Insight Mapping</p>

  <div class="features">
    <div class="feature">
      <span class="feature-badge">
        <svg width="24" height="26" viewBox="0 0 24 26" fill="none" stroke="var(--ink)" stroke-width="1.4">
          <path d="M3 1h13l5 5v19H3z"/><circle cx="9" cy="9" r="4"/><path d="M9 5v4h4"/>
          <path d="M7 22v-4M11 22v-6M15 22v-3M19 22v-8"/>
        </svg>
      </span>
      <span class="feature-label">Customized<br>Reporting</span>
    </div>
    <span class="divider"></span>
    <div class="feature">
      <span class="feature-badge">
        <svg width="24" height="26" viewBox="0 0 24 26" fill="none" stroke="var(--ink)" stroke-width="1.4">
          <rect x="3" y="3" width="16" height="21" rx="1"/><rect x="8" y="1" width="6" height="4"/>
          <path d="M6 10h2M10 10h6M6 14h2M10 14h6M6 18h2M10 18h3"/>
          <circle cx="18" cy="21" r="4" fill="var(--white)"/><path d="M16 21l1.5 1.5L20 20"/>
        </svg>
      </span>
      <span class="feature-label">Regulatory<br>Compliance</span>
    </div>
    <span class="divider"></span>
    <div class="feature">
      <span class="feature-badge">
        <svg width="26" height="24" viewBox="0 0 26 24" fill="none" stroke="var(--ink)" stroke-width="1.4">
          <rect x="1" y="3" width="20" height="14" rx="1"/><path d="M4 7h5M4 10h4M11 11l3-3 3 2 3-4"/>
          <path d="M4 15v-2M7 15v-3M10 15v-1"/>
          <circle cx="19" cy="17" r="5" fill="var(--white)"/><circle cx="19" cy="17" r="2"/>
        </svg>
      </span>
      <span class="feature-label">Real Time<br>Data Monitoring</span>
    </div>
  </div>

  <div class="website">
    <span class="globe">
      <svg width="22" height="22" viewBox="0 0 22 22" fill="none" stroke="var(--ink)" stroke-width="1.6">
        <circle cx="11" cy="11" r="9"/><ellipse cx="11" cy="11" rx="4" ry="9"/><path d="M2 11h18M4 6h14M4 16h14"/>
      </svg>
    </span>
    <span>www.<strong>brightmarkpartners-llc</strong>.example</span>
  </div>

  <div class="team-scene" role="img" aria-label="Illustration of a team reviewing charts and dashboards on a large curved display"></div>
</main>
</body>
</html>
```